Property Development company needs a business card design

i need a business card design for my company. we are a very small property developer specialising in land subdivisions in geelong Australia.

I would like to see a splash of brown yellow brown that is my favorite football team colors. (Pelmont) Its needs to be not offensive and slighlty subtle or mysterious or cheeky. I would like a white background with black writing.

Company is Varnel Property Developments. We dont have a logo - maybe a picture of a house /fence / gate / road could or couldnt work? I dont really know.

```html
<!DOCTYPE html>
<html lang="en">
<head>
<meta charset="utf-8">
<title>Varnel Property Developments – Business Card</title>
<link rel="stylesheet" href="https://fonts.googleapis.com/css2?family=Mulish:wght@400;700;800&display=swap">
<style>
  :root {
    --page-bg: #e9e9ea;
    --card-bg: #ffffff;
    --brown: #6a3a12;
    --brown-dark: #4e2a0c;
    --gold: #f2c21b;
    --ink: #1c1c1c;
    --icon: #2a2a2a;
  }
  * { margin: 0; padding: 0; box-sizing: border-box; }
  html, body {
    width: 1200px;
    height: 900px;
    overflow: hidden;
    background: var(--page-bg);
    font-family: "Mulish", sans-serif;
  }
  .card {
    position: absolute;
    left: 80px;
    top: 150px;
    width: 1040px;
    height: 600px;
    background: var(--card-bg);
    overflow: hidden;
    box-shadow: 0 10px 30px rgba(0,0,0,0.15);
  }
  .card__wave {
    position: absolute;
    left: 0;
    top: 0;
    width: 1040px;
    height: 600px;
  }
  .brand {
    position: absolute;
    left: 110px;
    top: 120px;
    display: flex;
    align-items: center;
    gap: 16px;
  }
  .brand__mark {
    width: 22px;
    height: 22px;
    background: var(--gold);
  }
  .brand__name {
    font-weight: 800;
    font-size: 30px;
    line-height: 1.15;
    color: var(--brown);
    letter-spacing: 0.5px;
  }
  .contact {
    position: absolute;
    left: 640px;
    top: 150px;
    color: var(--ink);
  }
  .contact__name {
    font-weight: 800;
    font-size: 40px;
    letter-spacing: 0.5px;
    margin-bottom: 26px;
  }
  .contact__list {
    list-style: none;
    font-size: 24px;
    line-height: 1.3;
  }
  .contact__item {
    display: flex;
    align-items: flex-start;
    gap: 14px;
    margin-bottom: 6px;
  }
  .contact__icon {
    width: 22px;
    height: 22px;
    flex: none;
    margin-top: 4px;
    fill: var(--icon);
  }
  .contact__icon--square {
    width: 18px;
    height: 18px;
    margin: 6px 2px 0;
    background: var(--icon);
  }
</style>
</head>
<body>
  <main class="card">
    <svg class="card__wave" viewBox="0 0 1040 600" aria-hidden="true">
      <defs>
        <linearGradient id="brownBand" x1="0" y1="0" x2="1" y2="1">
          <stop offset="0" stop-color="var(--brown)"/>
          <stop offset="1" stop-color="var(--brown-dark)"/>
        </linearGradient>
      </defs>
      <path d="M0,362 C210,318 390,358 540,455 C670,540 800,575 1040,580 L1040,600 L0,600 Z" fill="var(--gold)"/>
      <path d="M0,371 C210,328 385,367 532,462 C660,545 790,584 1040,590 L1040,600 L0,600 Z" fill="url(#brownBand)"/>
    </svg>

    <div class="brand">
      <span class="brand__mark"></span>
      <span class="brand__name">Varnel<br>Property Developments</span>
    </div>

    <section class="contact">
      <h1 class="contact__name">YOUR NAME</h1>
      <ul class="contact__list">
        <li class="contact__item">
          <svg class="contact__icon" viewBox="0 0 24 24" aria-hidden="true"><path d="M12 2a7 7 0 0 0-7 7c0 5 7 13 7 13s7-8 7-13a7 7 0 0 0-7-7zm0 9.5A2.5 2.5 0 1 1 12 6.5a2.5 2.5 0 0 1 0 5z"/></svg>
          <span>Street Address<br>city, Pos Code</span>
        </li>
        <li class="contact__item">
          <svg class="contact__icon" viewBox="0 0 24 24" aria-hidden="true"><path d="M6.6 10.8a15 15 0 0 0 6.6 6.6l2.2-2.2a1 1 0 0 1 1-.25 11.4 11.4 0 0 0 3.6.57 1 1 0 0 1 1 1V20a1 1 0 0 1-1 1A17 17 0 0 1 3 4a1 1 0 0 1 1-1h3.5a1 1 0 0 1 1 1c0 1.250.2 2.45.57 3.57a1 1 0 0 1-.25 1z"/></svg>
          <span>+000 1234 5555<br>+000 1234 6666</span>
        </li>
        <li class="contact__item">
          <svg class="contact__icon" viewBox="0 0 24 24" aria-hidden="true"><path d="M2 5h20v14H2zm2 2v.5l8 5 8-5V7l-8 5z"/></svg>
          <span>youremail@domain.com</span>
        </li>
        <li class="contact__item">
          <svg class="contact__icon" viewBox="0 0 24 24" aria-hidden="true"><path d="M12 2a10 10 0 1 0 0 20 10 10 0 0 0 0-20zm6.9 9h-3a15 15 0 0 0-1.3-5.6A8 8 0 0 1 18.9 11zM12 4.1c.9 1.2 1.8 3.6 1.9 6.9h-3.8c.1-3.3 1-5.7 1.9-6.9zM9.4 5.4A15 15 0 0 0 8.1 11h-3a8 8 0 0 1 4.3-5.6zM5.1 13h3a15 15 0 0 0 1.3 5.6A8 8 0 0 1 5.1 13zm6.9 6.9c-.9-1.2-1.8-3.6-1.9-6.9h3.8c-.1 3.3-1 5.7-1.9 6.9zm2.6-1.3a15 15 0 0 0 1.3-5.6h3a8 8 0 0 1-4.3 5.6z"/></svg>
          <span>www.yourdomain.com</span>
        </li>
        <li class="contact__item">
          <span class="contact__icon contact__icon--square"></span>
          <span>your social handle</span>
        </li>
      </ul>
    </section>
  </main>
</body>
</html>
```